DRIFTFRAME studio

Design to be modern with colours of logo, maybe orange background. Include name, position, phone/WhatsApp email/web. Specialises in long form TIMELAPSE

Contact Information for Business Card

Marcel Okoro, filmmaker,/photographer, phone/WhatsApp +971529386047, email - marcel@driftframestudio.com www.driftframestudio.com, instagram @driftframestudio

Font styles to use
Sans Serif

Requirements
Must have
• Fresh, bright, modern, original
Marcel Okoro - Filmmaker/Photographer
Phone/WhatsApp +971 529 38 6047
email - marcel@driftfarmestudio.com
Web - driftfarmestudio.com
PoBox 584319, Dubai, UAE
instagram - driftframestudio
Should not have
• solid black background

```html
<!DOCTYPE html>
<html lang="en">
<head>
<meta charset="UTF-8">
<title>DRIFTFRAME studio – Business Card</title>
<link href="https://fonts.googleapis.com/css2?family=Montserrat:wght@700;800&family=Roboto:wght@400;500&display=swap" rel="stylesheet">
<style>
  :root {
    --orange: #f47920;
    --charcoal-top: #2a2a2e;
    --charcoal-bottom: #1a1a1d;
    --white: #ffffff;
    --stage: #e9e9e9;
  }
  * { box-sizing: border-box; margin: 0; padding: 0; }
  html, body {
    width: 1200px; height: 900px; overflow: hidden;
    background: var(--stage);
  }
  .canvas { position: relative; width: 1200px; height: 900px; }

  .card {
    position: absolute;
    width: 700px; height: 400px;
    box-shadow: 0 14px 30px rgba(0,0,0,.25);
    overflow: hidden;
  }

  .brand {
    position: absolute; display: flex; align-items: center; gap: 16px;
    font-family: "Montserrat", sans-serif; font-weight: 800;
    letter-spacing: .5px; white-space: nowrap;
  }
  .brand__name { display: flex; flex-direction: column; line-height: 1; }
  .brand__dot {
    width: 54px; height: 54px; border-radius: 50%;
    border: 5px solid currentColor; flex: none;
  }

  /* Front */
  .card--front { left: 80px; top: 50px; background: var(--orange); }
  .card--front .brand {
    color: var(--white); font-size: 50px;
    left: 50%; top: 50%; transform: translate(-50%, -50%);
  }
  .card--front .brand__dot { width: 72px; height: 72px; border-width: 6px; }

  /* Back */
  .card--back {
    left: 420px; top: 460px;
    background: linear-gradient(160deg, var(--charcoal-top), var(--charcoal-bottom));
  }
  .card--back .brand {
    color: var(--white); font-size: 28px; gap: 14px;
    left: 48px; top: 170px;
  }
  .card--back .brand__dot { width: 46px; height: 46px; border-width: 4px; border-color: var(--orange); }
  .divider {
    position: absolute; left: 330px; top: 105px;
    width: 2px; height: 160px; background: var(--orange);
  }
  .contact {
    position: absolute; left: 360px; top: 96px;
    font-family: "Roboto", sans-serif; color: var(--white);
  }
  .contact__name {
    font-family: "Montserrat", sans-serif; font-weight: 800;
    color: var(--orange); font-size: 25px; line-height: 1.1;
  }
  .contact__role { font-size: 14px; margin-top: 4px; }
  .contact__list { list-style: none; margin-top: 22px; }
  .contact__item {
    display: flex; align-items: center; gap: 8px;
    font-size: 14px; line-height: 24px;
  }
  .contact__icons { display: flex; gap: 4px; width: 34px; justify-content: flex-end; }
  .icon { width: 12px; height: 12px; fill: var(--orange); flex: none; }
  .icon--circle { border-radius: 50%; border: 2px solid var(--orange); }
  .icon--square { border-radius: 2px; border: 2px solid var(--orange); }

  .stripe { position: absolute; left: 0; bottom: 0; width: 700px; height: 40px; }
</style>
</head>
<body>
<div class="canvas">

  <section class="card card--front">
    <div class="brand"><span class="brand__dot"></span><span class="brand__name"><span>DRIFTFRAME</span><span>studio</span></span></div>
  </section>

  <section class="card card--back">
    <div class="brand"><span class="brand__dot"></span><span class="brand__name"><span>DRIFTFRAME</span><span>studio</span></span></div>

    <div class="divider"></div>

    <div class="contact">
      <div class="contact__name">Marcel Okoro</div>
      <div class="contact__role">Filmmaker,/Photographer</div>
      <ul class="contact__list">
        <li class="contact__item">
          <span class="contact__icons">
            <svg class="icon" viewBox="0 0 24 24" aria-hidden="true"><path d="M6.6 10.8a15 15 0 0 0 6.6 6.6l2.2-2.2a1 1 0 0 1 1-.25 11.4 11.4 0 0 0 3.6.57 1 1 0 0 1 1 1V20a1 1 0 0 1-1 1A17 17 0 0 1 3 4a1 1 0 0 1 1-1h3.5a1 1 0 0 1 1 1c0 1.25.2 2.45.57 3.57a1 1 0 0 1-.25 1z"/></svg>
            <span class="icon icon--circle"></span>
          </span>+971529386047
        </li>
        <li class="contact__item">
          <span class="contact__icons">
            <svg class="icon" viewBox="0 0 24 24" aria-hidden="true"><path d="M2 5h20v14H2zm2 2v.5l8 5 8-5V7l-8 5z"/></svg>
          </span>marcel@driftframestudio.com
        </li>
        <li class="contact__item">
          <span class="contact__icons">
            <svg class="icon" viewBox="0 0 24 24" aria-hidden="true"><circle cx="12" cy="12" r="10" fill="none" stroke="#f47920" stroke-width="2.5"/><path d="M2 12h20M12 2c3 3 3 17 0 20M12 2c-3 3-3 17 0 20" fill="none" stroke="#f47920" stroke-width="2"/></svg>
          </span>www.driftframestudio.com
        </li>
        <li class="contact__item">
          <span class="contact__icons"><span class="icon icon--square"></span></span>@driftframestudio
        </li>
      </ul>
    </div>

    <svg class="stripe" viewBox="0 0 700 40" aria-hidden="true">
      <rect x="0" y="30" width="540" height="10" fill="#f47920"/>
      <polygon points="548,40 556,22 582,22 574,40" fill="#f47920"/>
      <polygon points="590,40 598,22 624,22 616,40" fill="#f47920"/>
      <polygon points="632,40 640,22 666,22 658,40" fill="#f47920"/>
      <polygon points="674,40 682,22 700,22 700,40" fill="#f47920"/>
    </svg>
  </section>

</div>
</body>
</html>
```